Electrical Industry Newletter Design Project PSD format with layers

The Name of the newsletter is:
A "Pulse" of the Hour
-This is a bi monthly newsletter focused on the Electrical and Cabling Industry
"Pulse" of course is a play on words referring to a Sine wave
We are looking for a creative yet professional looking newsletter. Our targeted audience are professional consulting engineers, architects, & property owners/manager.
We are looking for a unique logo for the newsletters name "Pull of the Hours" with the subtext being "Electrical & Cabling Industry"
We envision the incorporations of the sin wave into the logo and other such associated symbols associated with our industry.
Note: the Newsletter is going to be brought to them by our company KAV Electric. Our logo should be incorporated near the top of the newsletter but be less prominent.
Each issue is going to be a "Vol" Hence the Vol number should be editable.
There should be a featured article area labeled
-Whats Happening
-This section should have a spot for a relevant pictures
There should be a side section labeled
-Code Alert!
-Just for laughs
-This section should be available to place a relevant picture or comic strips of sorts.
The should be a section labeled
-Project Profile (This will be where we profile a recent project with pictures
You have total artistic license with this project, I know you will produce a great work of art!
Updates
What happened to all those creative juices??? Added Thursday, April 27, 2017
Target Market(s)
Consulting Engineers, Architects, Specifiers, Building Owners & Managers
Industry/Entity Type
Electrical
Look and feel

```html
<!DOCTYPE html>
<html lang="en">
<head>
<meta charset="utf-8">
<title>Pulse of the Hours — Vol 01</title>
<link rel="stylesheet" href="https://fonts.googleapis.com/css2?family=Oswald:wght@500;600&family=PT+Sans:ital,wght@0,400;0,700;1,400;1,700&display=swap">
<style>
:root{
  --ink:#231f20;
  --gold:#e3b52c;
  --gold-band:#dcc46a;
  --gold-frame:#c9a227;
  --paper:#ffffff;
  --text-light:#f2f2f2;
  --text-dark:#222;
}
*{margin:0;padding:0;box-sizing:border-box}
html,body{width:1200px;height:2917px;overflow:hidden;background:var(--paper)}
body{position:relative;font-family:"PT Sans",Arial,sans-serif;color:var(--text-dark)}
.bands{position:absolute;left:0;top:0;width:1200px;height:2917px}
.masthead-name{position:absolute;left:238px;top:52px;font-family:"Oswald",Arial,sans-serif;font-weight:600;font-size:32px;letter-spacing:.5px;color:var(--ink);line-height:1}
.masthead-sub{position:absolute;left:238px;top:96px;font-family:"PT Sans",Arial,sans-serif;font-size:13px;letter-spacing:1px;color:var(--gold);text-transform:uppercase}
.masthead-mark{position:absolute;left:64px;top:48px;width:150px;height:58px;background:var(--ink)}
.guide-v{position:absolute;left:52px;top:0;height:195px;border-left:2px dashed var(--ink)}
.guide-h{position:absolute;left:0;top:78px;width:228px;border-top:2px dashed var(--ink)}
.vol-box{position:absolute;left:560px;top:0;width:82px;height:117px;background:var(--ink);color:#fff;text-align:center;font-family:"Oswald",Arial,sans-serif}
.vol-box .label{display:block;font-size:22px;margin-top:14px;line-height:1}
.vol-box .num{display:block;font-size:46px;line-height:1;margin-top:10px}
.sponsor{position:absolute;right:52px;top:30px;text-align:right}
.sponsor .by{font-size:15px;color:var(--text-dark)}
.sponsor .name{margin-top:6px;font-family:"PT Sans",Arial,sans-serif;font-weight:700;font-size:22px;letter-spacing:1px;color:var(--ink);display:flex;align-items:center;gap:10px;justify-content:flex-end}
.sponsor .name::before{content:"";width:18px;height:18px;background:var(--ink)}
.section-title{position:absolute;right:52px;font-family:"Oswald",Arial,sans-serif;font-weight:600;font-size:31px;text-transform:uppercase;line-height:1}
.section-title.gold{color:var(--gold)}
.section-title.dark{color:var(--ink)}
.copy{position:absolute;font-size:19px;line-height:24.6px}
.copy.light{color:var(--text-light)}
.copy.justify{text-align:justify}
.copy.italic{font-style:italic}
.copy.highlight{color:var(--gold);font-weight:700;font-style:italic}
.photo{position:absolute;border:4px solid var(--gold-frame)}
.photo.plain{border:none}
.tag{position:absolute;left:0;top:1064px;width:292px;height:47px;background:var(--gold);font-family:"Oswald",Arial,sans-serif;font-weight:600;font-size:29px;color:var(--ink);padding-left:52px;line-height:47px}
</style>
</head>
<body>
<svg class="bands" viewBox="0 0 1200 2917" aria-hidden="true">
  <polygon points="0,230 1200,152 1200,885 0,1021" fill="#231f20"/>
  <polygon points="0,1498 1200,1362 1200,1760 0,1906" fill="#dcc46a"/>
  <polygon points="0,1906 1200,1760 1200,2917 0,2917" fill="#231f20"/>
</svg>

<header>
  <div class="guide-v"></div>
  <div class="guide-h"></div>
  <div class="masthead-mark"></div>
  <div class="masthead-name">PULSE OF THE HOURS</div>
  <div class="masthead-sub">Electrical &amp; Cabling Industry</div>
  <div class="vol-box"><span class="label">VOL</span><span class="num">01</span></div>
  <div class="sponsor">
    <div class="by">brought to you by</div>
    <div class="name">KAV ELECTRIC LLC</div>
  </div>
</header>

<section class="whats-happening">
  <h2 class="section-title gold" style="top:197px">What's Happening</h2>
  <div class="photo" style="left:74px;top:263px;width:307px;height:307px;background:linear-gradient(135deg,#e6e2d6,#7d7a6f 55%,#2c2a26)" role="img" aria-label="Network switch with patch cables plugged in"></div>
  <div class="photo" style="left:74px;top:618px;width:307px;height:308px;background:linear-gradient(180deg,#9cc0e4,#d6e4f2 60%,#7a8f6a)" role="img" aria-label="High-voltage transmission tower against the sky"></div>
  <p class="copy light" style="left:461px;top:238px;width:687px">Lorem ipsum dolor sit amet, consectetur adipiscing elit. Integer bibendum eros in diam aliquet, et commodo dolor venenatis. Nulla eleifend sapien sit amet odio imperdiet efficitur. Interdum et malesuada fames ac ante ipsum primis in faucibus. Cras eget massa lorem.<br>Quisque augue enim, pellentesque nec mi vitae, tincidunt gravida lectus. Cras facilisis varius iaculis. Nunc turpis tortor, blandit eget tristique et, dapibus sit amet dolor.<br>Nam at maximus tellus. In hac habitasse platea dictumst. Sed maximus eget leo ac vulputate. Morbi hendrerit mauris et nunc varius, vitae aliquet eros dictum. Aenean tempus mauris vitae ligula interdum, id fermentum enim ullamcorper. Morbi nec fringilla sem.<br>Proin ultrices urna sit amet dapibus viverra. Donec fermentum commodo tortor eu eleifend. Nunc at nisl ut ante viverra auctor.</p>
  <p class="copy light" style="left:461px;top:609px;width:687px">Lorem ipsum dolor sit amet, consectetur adipiscing elit. Integer bibendum eros in diam aliquet, et commodo dolor venenatis. Nulla eleifend sapien sit amet odio imperdiet efficitur. Interdum et malesuada fames ac ante ipsum primis in faucibus. Cras eget massa lorem.<br>Quisque augue enim, pellentesque nec mi vitae, tincidunt gravida lectus. Cras facilisis varius iaculis. Nunc turpis tortor, blandit eget tristique et, dapibus sit amet dolor.<br>Nam at maximus tellus. In hac habitasse platea dictumst. Sed maximus eget leo ac vulputate. Morbi hendrerit mauris et nunc varius, vitae aliquet eros dictum. Aenean tempus mauris vitae ligula interdum, id fermentum enim ullamcorper. Morbi nec fringilla sem.</p>
</section>

<section class="code-alert">
  <h2 class="tag">CODE ALERT!</h2>
  <p class="copy italic justify" style="left:58px;top:1141px;width:542px">Lorem ipsum dolor sit amet, consectetur adipiscing elit. Integer bibendum eros in diam aliquet, et commodo dolor venenatis. Nulla eleifend sapien sit amet odio imperdiet efficitur. Interdum et malesuada fames ac ante ipsum primis in faucibus. Cras eget massa lorem.<br>Quisque augue enim, pellentesque nec mi vitae, tincidunt gravida lectus. Cras facilisis varius iaculis. Nunc turpis tortor, blandit eget tristique et, dapibus sit amet dolor.<br>Nam at maximus tellus. In hac habitasse platea dictumst. Sed maximus eget leo ac vulputate. Morbi hendrerit mauris et nunc varius, vitae aliquet eros dictum.</p>
  <div class="photo plain" style="left:710px;top:982px;width:380px;height:428px;background:linear-gradient(90deg,#3a8fd8,#a24fc0 25%,#3b3b3b 45%,#d8338f 60%,#e6cf2a 78%,#2f9a44)" role="img" aria-label="Bundle of colourful network patch cables standing upright"></div>
</section>

<section class="just-for-laughs">
  <h2 class="section-title dark" style="top:1489px">Just for Laughs</h2>
  <div class="photo plain" style="left:88px;top:1440px;width:408px;height:456px;background:linear-gradient(180deg,#d9c3a8,#b89778 40%,#2e3644)" role="img" aria-label="Laughing man in a suit jacket"></div>
  <p class="copy justify" style="left:619px;top:1531px;width:529px">Lorem ipsum dolor sit amet, consectetur adipiscing elit. Integer bibendum eros in diam aliquet, et commodo dolor venenatis. Nulla eleifend sapien sit amet odio imperdiet efficitur. Interdum et malesuada fames ac ante ipsum primis in faucibus. Cras eget massa lorem.<br>Quisque augue enim, pellentesque nec mi vitae, tincidunt gravida lectus. Cras facilisis varius iaculis. Nunc turpis tortor, blandit eget tristique et, dapibus sit amet dolor.<br>&nbsp;ullamcorper.<br>Morbi nec fringilla sem.</p>
</section>

<section class="whats-happening">
  <h2 class="section-title gold" style="top:1929px">What's Happening</h2>
  <div class="photo" style="left:74px;top:1945px;width:307px;height:311px;background:linear-gradient(135deg,#e6e2d6,#7d7a6f 55%,#2c2a26)" role="img" aria-label="Network switch with patch cables plugged in"></div>
  <div class="photo" style="left:74px;top:2301px;width:307px;height:305px;background:linear-gradient(180deg,#9cc0e4,#d6e4f2 60%,#7a8f6a)" role="img" aria-label="High-voltage transmission tower against the sky"></div>
  <p class="copy light" style="left:461px;top:1970px;width:687px">Lorem ipsum dolor sit amet, consectetur adipiscing elit. Integer bibendum eros in diam aliquet, et commodo dolor venenatis. Nulla eleifend sapien sit amet odio imperdiet efficitur. Interdum et malesuada fames ac ante ipsum primis in faucibus. Cras eget massa lorem.<br>Quisque augue enim, pellentesque nec mi vitae, tincidunt gravida lectus. Cras facilisis varius iaculis. Nunc turpis tortor, blandit eget tristique et, dapibus sit amet dolor.<br>Nam at maximus tellus. In hac habitasse platea dictumst. Sed maximus eget leo ac vulputate. Morbi hendrerit mauris et nunc varius, vitae aliquet eros dictum. Aenean tempus mauris vitae ligula interdum, id fermentum enim ullamcorper. Morbi nec fringilla sem.<br>Proin ultrices urna sit amet dapibus viverra. Donec fermentum commodo tortor eu eleifend. Nunc at nisl ut ante viverra auctor.</p>
  <p class="copy highlight justify" style="left:461px;top:2316px;width:687px">Lorem ipsum dolor sit amet, consectetur adipiscing elit. Integer bibendum eros in diam aliquet, et commodo dolor venenatis. Nulla eleifend sapien sit amet odio imperdiet efficitur. Interdum et malesuada fames ac ante ipsum primis in faucibus. Cras eget massa lorem.<br>Quisque augue enim, pellentesque nec mi vitae, tincidunt gravida lectus. Cras facilisis varius iaculis. Nunc turpis tortor, blandit eget tristique et, dapibus sit amet dolor.</p>
</section>

<svg class="bands" viewBox="0 0 1200 2917" role="img" aria-label="Bright loading bay of a warehouse with a truck at the dock">
  <defs>
    <linearGradient id="bay" x1="0" y1="0" x2="0" y2="1">
      <stop offset="0" stop-color="#1d3550"/>
      <stop offset=".55" stop-color="#6f93b4"/>
      <stop offset="1" stop-color="#c7d7e4"/>
    </linearGradient>
  </defs>
  <polygon points="0,2665 1200,2518 1200,2917 0,2917" fill="url(#bay)"/>
</svg>
</body>
</html>
```